Innovative mission-driven diversity services company needs launch brochure

Two-sided 8 1/5" x 11" document to demonstrate a new program.

Target Market(s)

Chief Diversity Officers and Hiring Managers at advertising/communications agencies who are looking to attract and hire recently graduated/about to graduate African American students

Industry/Entity Type

It Company

Requirements
Must have
• a very contemporary feel that will well represent the vibrancy, energy, and identity of the African American student population. This is a cause driven organization and that passion and purpose should be conveyed while recognizing that the target audience are corporate executives.

```html
<!DOCTYPE html>
<html lang="en">
<head>
<meta charset="utf-8">
<title>Narrowing the Racial Diversity Gap</title>
<link href="https://fonts.googleapis.com/css2?family=Montserrat:wght@600;700;800&family=Oswald:wght@500;600;700&family=Roboto:wght@400;500;700&family=Roboto+Slab:wght@600;700&family=Libre+Baskerville:ital,wght@1,700&display=swap" rel="stylesheet">
<style>
:root{
  --ink:#000;
  --blue:#1766c2;
  --blue-deep:#0f4fa6;
  --blue-num:#1a7fc9;
  --yellow:#f7e400;
  --orange:#e84e1b;
  --text:#333;
  --muted:#555;
  --rule:#d6d6d6;
  --white:#fff;
}
*{margin:0;padding:0;box-sizing:border-box}
html,body{width:960px;height:1200px;overflow:hidden;background:var(--ink)}
body{position:relative;font-family:"Roboto",sans-serif;color:var(--text)}
.page-number{position:absolute;top:10px;right:12px;font-family:"Oswald",sans-serif;font-weight:500;font-size:30px;color:var(--blue-num)}
.sheet{position:absolute;left:136px;top:118px;width:701px;height:992px;background:var(--white);overflow:hidden}
.hero{position:absolute;left:0;top:0;width:701px;height:403px;background:linear-gradient(135deg,var(--blue-deep),var(--blue) 45%,#2a86d8 75%,var(--blue))}
.brand{position:absolute;left:52px;top:38px;font-family:"Montserrat",sans-serif;font-weight:800;color:var(--white);font-size:66px;line-height:.95;letter-spacing:-2px}
.hero-title{position:absolute;left:335px;top:33px;font-family:"Montserrat",sans-serif;font-weight:700;color:var(--white);font-size:30px;line-height:1.08}
.hero-sub{position:absolute;left:335px;top:105px;width:290px;font-family:"Montserrat",sans-serif;font-weight:700;color:var(--yellow);font-size:13px;line-height:1.25}
.hero-rule{position:absolute;left:68px;top:168px;width:570px;height:1px;background:rgba(255,255,255,.45)}
.hero-intro{position:absolute;left:40px;top:180px;width:621px;text-align:center;color:var(--white);font-size:13.4px;line-height:1.35}
.chart{position:absolute;left:48px;top:234px;width:605px;height:264px;background:var(--white)}
.chart-title{position:absolute;top:22px;width:100%;text-align:center;color:var(--blue);font-weight:700;font-size:15px;letter-spacing:.2px}
.year{position:absolute;top:50px;font-weight:500;font-size:17px;color:#444}
.gridline{position:absolute;left:34px;width:524px;height:1px;background:#eee}
.baseline{position:absolute;left:34px;top:196px;width:524px;height:1.5px;background:#999}
.bar{position:absolute;background:var(--orange);color:var(--white);font-family:"Oswald",sans-serif;font-weight:600;font-size:23px;text-align:center;display:flex;align-items:flex-end;justify-content:center;padding-bottom:8px;width:78px}
.bar-label{position:absolute;top:212px;width:120px;text-align:center;font-weight:700;font-size:10px;line-height:1.3;color:#555;letter-spacing:.3px}
.body-copy{position:absolute;left:48px;top:520px;width:610px;font-size:12.2px;line-height:1.25;color:var(--text)}
.body-copy p+p{margin-top:4px}
.section-head{position:absolute;left:0;width:701px;text-align:center;font-family:"Oswald",sans-serif;font-weight:700;font-size:21px;letter-spacing:-.6px;color:#2a2a2a;text-transform:uppercase}
.article{position:absolute;left:50px;top:632px;width:246px;height:123px;border:1px solid #999;padding:8px 14px}
.article-tag{font-family:"Roboto Slab",serif;font-weight:700;font-size:6.5px;color:#888}
.article-headline{margin-top:5px;font-family:"Roboto Slab",serif;font-weight:700;font-size:17px;line-height:1.12;color:#222}
.share{display:flex;gap:2px;margin-top:5px}
.share span{font-size:5px;font-weight:700;color:var(--white);padding:3px 5px}
.share .s1{background:#3b5a9a}.share .s2{background:#4aa3e0}.share .s3{background:#e04a2a}
.byline{margin-top:9px;font-size:6px;color:#777}
.quote-box{position:absolute;left:310px;top:632px;width:350px;height:123px;border:1px solid #999}
.portrait{position:absolute;left:10px;top:13px;width:96px;height:96px;border-radius:50%;background:radial-gradient(circle at 50% 40%,#c9a58c,#7a6a60 60%,#3c3c3c)}
.quote{position:absolute;left:118px;top:12px;width:222px;font-family:"Libre Baskerville",serif;font-style:italic;font-weight:700;font-size:10.3px;line-height:1.5;color:#333}
.quote-mark{position:absolute;left:244px;top:74px;font-family:"Oswald",sans-serif;font-weight:700;font-size:72px;line-height:1;color:#eee}
.speaker{position:absolute;left:116px;top:79px;font-weight:700;color:#222}
.speaker .name{font-size:13px}
.speaker .role{font-size:10.5px;margin-top:1px}
.reason{position:absolute;top:831px;width:177px}
.reason-image{height:74px}
.reason p{margin-top:15px;font-size:12px;line-height:1.3;color:#444}
.bottom-band{position:absolute;left:0;bottom:0;width:701px;height:10px;background:var(--blue)}
</style>
</head>
<body>
<div class="page-number">24</div>
<main class="sheet">
  <header class="hero">
    <div class="brand">Uplift<br>LLC</div>
    <h1 class="hero-title">Narrowing the<br>Racial Diversity Gap</h1>
    <p class="hero-sub">A powerful new approach to increasing the African-American employment rate in the communications industry</p>
    <div class="hero-rule"></div>
    <p class="hero-intro">Despite efforts to increase participation, African-American rates of employment in the communications industry have actually declined over the past decade</p>
  </header>

  <section class="chart" aria-label="African-American proportion of workforce">
    <h2 class="chart-title">AFRICAN-AMERICAN PROPORTION OF WORKFORCE*</h2>
    <div class="year" style="left:140px">2015</div>
    <div class="year" style="left:428px">2016</div>
    <div class="gridline" style="top:88px"></div>
    <div class="gridline" style="top:116px"></div>
    <div class="gridline" style="top:144px"></div>
    <div class="gridline" style="top:172px"></div>
    <div class="bar" style="left:52px;top:87px;height:109px">11%</div>
    <div class="bar" style="left:173px;top:130px;height:66px">7%</div>
    <div class="bar" style="left:340px;top:73px;height:123px">12%</div>
    <div class="bar" style="left:461px;top:148px;height:48px">5%</div>
    <div class="baseline"></div>
    <div class="bar-label" style="left:31px">OVERALL<br>WORKFORCE</div>
    <div class="bar-label" style="left:152px">COMMUNICATIONS<br>INDUSTRY</div>
    <div class="bar-label" style="left:317px">OVERALL<br>WORKFORCE</div>
    <div class="bar-label" style="left:438px">COMMUNICATIONS<br>INDUSTRY</div>
  </section>

  <div class="body-copy">
    <p>While the communications agency hiring rate of people of Hispanic or Asian origin has reached parity with their overall workforce participation rates, African-American participation has actually dropped by nearly a third.</p>
    <p>Communications agencies have identified this gap as a critical issue but are falling further behind on AA hiring.<br>*REFERENCE TO COME</p>
  </div>

  <h2 class="section-head" style="top:592px">Clients have now begun to directly exert pressure on the industry</h2>

  <article class="article">
    <div class="article-tag">BRANDS</div>
    <h3 class="article-headline">Harvest Fields Foods Insists That Its Future Agencies Meet Specific Diversity Quotas</h3>
    <div class="share"><span class="s1">Share</span><span class="s2">Post</span><span class="s3">More</span></div>
    <div class="byline">By Jon Carver on Aug. 31, 2016 - 11:06 AM &nbsp; Comment</div>
  </article>

  <aside class="quote-box">
    <div class="portrait" role="img" aria-label="Portrait photo of the speaker"></div>
    <p class="quote">“In order to push yourself to have a more diverse work force you have to be intentional about it — and nothing will drive intent faster than a client’s dollar”</p>
    <div class="quote-mark">”</div>
    <div class="speaker"><div class="name">Dana Whitfield</div><div class="role">President &amp; CEO, AAIA</div></div>
  </aside>

  <h2 class="section-head" style="top:790px">Why are communications agencies failing to increase the AA hiring rate?</h2>

  <div class="reason" style="left:53px">
    <div class="reason-image" role="img" aria-label="Photo of a panel discussion on stage" style="background:linear-gradient(180deg,#b8556a,#6d5a6e 55%,#2b2b2b)"></div>
    <p>An industry too inwardly focused to realize that it can be offputting</p>
  </div>
  <div class="reason" style="left:268px">
    <div class="reason-image" role="img" aria-label="Illustration of two facing profiles over a striped flag" style="background:linear-gradient(90deg,#d9a67a,#eee9df 50%,#c9655a)"></div>
    <p>Assuming barriers to hiring all people of color are the same and are not unique to each group</p>
  </div>
  <div class="reason" style="left:486px">
    <div class="reason-image" role="img" aria-label="Photo of a graduate holding a sign" style="background:radial-gradient(circle at 50% 60%,#3a3a3a,#8a8a8a 45%,#f2f2f2 75%)"></div>
    <p>Dramatic disconnection from the most critical candidate pool that can provide an immediate &amp; lasting impact</p>
  </div>

  <div class="bottom-band"></div>
</main>
</body>
</html>
```